Bright Fern Custom Homes business card. Double sided. Modern. professional

Bright Fern Custom Homes
contemporary modern design with our logo /
Double sided with all our contact information
Use same Green colors as in our Logo. Contemporary logo that grabs your attention. Visually pleasing and balanced. Easy to read, and Vibrant. Would love an option for rounded edges. Embossed logo would be amazing.
Contact Information for Business Card
Dana Welk Owner / General Contractor Bright Fern Custom Homes p: 704.552.1830 m: 912.648.2071 e: brightferncustomhomes@mailbox.example w: www.brightferncustomhomes.example 218 Pryor Meadow Lane Larkfield, NV 29041

```html
<!DOCTYPE html>
<html lang="en">
<head>
<meta charset="utf-8">
<title>Bright Fern Custom Homes – Business Card</title>
<link rel="stylesheet" href="https://fonts.googleapis.com/css2?family=Fira+Sans:wght@700&family=Quicksand:wght@500;700&family=Cinzel:wght@500&display=swap">
<style>
  :root {
    --backdrop: #6c8a3c;
    --card: #eef1e2;
    --card-light: #f3f6e8;
    --green: #6e8e34;
    --green-soft: #8aa656;
    --ink: #3b3b33;
  }
  * { box-sizing: border-box; margin: 0; padding: 0; }
  html, body { width: 1200px; height: 1200px; overflow: hidden; }
  body {
    background: var(--backdrop);
    position: relative;
    font-family: "Quicksand", sans-serif;
    color: var(--ink);
  }
  .card {
    position: absolute;
    left: 160px;
    width: 880px;
    height: 500px;
    border-radius: 26px;
    background: linear-gradient(100deg, var(--card) 0%, var(--card-light) 100%);
    overflow: hidden;
    box-shadow: 0 14px 30px rgba(0,0,0,0.22);
  }
  .card--front { top: 76px; }
  .card--back { top: 624px; }

  .guides { position: absolute; inset: 0; }

  .contact-name {
    position: absolute; left: 76px; top: 112px;
    font-family: "Fira Sans", sans-serif; font-weight: 700;
    font-size: 43px; color: var(--green); letter-spacing: 0.3px;
  }
  .contact-role {
    position: absolute; left: 78px; top: 178px;
    font-size: 22px; font-weight: 500; line-height: 33px; color: var(--ink);
  }
  .divider {
    position: absolute; left: 76px; top: 276px;
    width: 140px; height: 2px; background: var(--green-soft);
  }
  .contact-list {
    position: absolute; left: 74px; top: 320px; list-style: none;
  }
  .contact-list li {
    display: flex; align-items: center; height: 46px;
    font-size: 25px; font-weight: 500; white-space: nowrap;
  }
  .contact-list svg { width: 34px; height: 34px; margin-right: 19px; flex: none; }
  .dot { display: inline-block; width: 6px; height: 6px; border-radius: 50%; background: var(--ink); margin: 0 20px; }

  .brand {
    position: absolute; text-align: center;
    font-family: "Cinzel", serif; font-weight: 500; color: var(--green);
    white-space: nowrap;
  }
  .brand__mark { position: absolute; border-radius: 50%; background: var(--green); }
  .brand__name, .brand__sub { position: absolute; left: 0; right: 0; text-align: center; }
  .brand__sub { text-transform: uppercase; }

  .brand--small { left: 540px; top: 58px; width: 270px; height: 200px; }
  .brand--small .brand__mark { left: 85px; top: 0; width: 120px; height: 120px; }
  .brand--small .brand__name { top: 140px; font-size: 28px; line-height: 32px; letter-spacing: 1px; }
  .brand--small .brand__sub { top: 174px; font-size: 10px; line-height: 12px; letter-spacing: 5px; }

  .brand--large { left: 70px; top: 62px; width: 480px; height: 340px; }
  .brand--large .brand__mark { left: 130px; top: 0; width: 220px; height: 220px; }
  .brand--large .brand__name { top: 252px; font-size: 48px; line-height: 54px; letter-spacing: 2px; }
  .brand--large .brand__sub { top: 312px; font-size: 15px; line-height: 18px; letter-spacing: 10px; }

  .website {
    position: absolute; left: 80px; top: 410px;
    font-weight: 700; font-size: 22px; letter-spacing: 1.6px; color: var(--green);
    white-space: nowrap;
  }
</style>
</head>
<body>

<section class="card card--front" aria-label="Business card front">
  <svg class="guides" width="880" height="500" viewBox="0 0 880 500" aria-hidden="true">
    <g stroke="#7a9a3e" stroke-width="2">
      <line x1="36" y1="60" x2="364" y2="60"/>
      <line x1="74" y1="0" x2="74" y2="78"/>
      <line x1="327" y1="0" x2="327" y2="78"/>
      <line x1="770" y1="438" x2="880" y2="438"/>
      <line x1="807" y1="420" x2="807" y2="500"/>
    </g>
  </svg>

  <h1 class="contact-name">Dana Welk</h1>
  <p class="contact-role">Owner / General Contractor<br>Bright Fern Custom Homes</p>
  <div class="divider"></div>

  <ul class="contact-list">
    <li>
      <svg viewBox="0 0 34 34" aria-hidden="true"><circle cx="17" cy="17" r="17" fill="#6e8e34"/>
        <path d="M12 21h10l-1.5-2v-4a3.5 3.5 0 0 0-7 0v4z M15.5 22.5h3a1.5 1.5 0 0 1-3 0z" fill="#fff"/></svg>
      p. 704.552.1830<span class="dot"></span>m. 912.648.2071
    </li>
    <li>
      <svg viewBox="0 0 34 34" aria-hidden="true"><circle cx="17" cy="17" r="17" fill="#6e8e34"/>
        <rect x="9" y="11" width="16" height="12" rx="1.5" fill="none" stroke="#fff" stroke-width="1.8"/>
        <path d="M9.5 12l7.5 6 7.5-6" fill="none" stroke="#fff" stroke-width="1.8"/></svg>
      brightferncustomhomes@mailbox.example
    </li>
    <li>
      <svg viewBox="0 0 34 34" aria-hidden="true"><circle cx="17" cy="17" r="17" fill="#6e8e34"/>
        <path d="M17 8a5 5 0 0 0-5 5c0 4 5 10 5 10s5-6 5-10a5 5 0 0 0-5-5z" fill="#fff"/>
        <circle cx="17" cy="13" r="1.8" fill="#6e8e34"/><rect x="10" y="24" width="14" height="2" fill="#fff"/></svg>
      218 Pryor Meadow Lane Larkfield, NV 29041
    </li>
  </ul>

  <div class="brand brand--small">
    <span class="brand__mark" aria-hidden="true"></span>
    <span class="brand__name">Bright Fern</span>
    <span class="brand__sub">Custom Homes</span>
  </div>
</section>

<section class="card card--back" aria-label="Business card back">
  <div class="brand brand--large">
    <span class="brand__mark" aria-hidden="true"></span>
    <span class="brand__name">Bright Fern</span>
    <span class="brand__sub">Custom Homes</span>
  </div>
  <p class="website">www.brightferncustomhomes.example</p>
</section>

</body>
</html>
```